Ashworth Web Design Project

I need the front page and an internal page designed for this client's website. The logo is attached. Obviously the colors have to go with and/or work with the logo colors. I also attached a very rough brochure layout to help you see the direction we're going in with print materials. The rough site map is also attached. I see a slider on the homepage, the art for which I may come back to you to create. This clinic is in a very high end Dallas neighborhood. The hook is that it's a primary care and urgent facility with convenient hours.

I don't know how much this impacts your design, but this will be a Wordpress site and I'm using a framework called Struxo (struxo-demo.example). If Struxo proves to be inflexible, I'll have to get a template that allows me to execute your design.

This site (http://oakbendcareclinic.example) has the type and quality of content I will eventually have on the Ashworth site.

I just revised the brief for this project. I added the site map and added details to the overview and the "Must Have" section. Thank you for revisiting the brief. 

Reason: Christmas was a bad time to end it.

Target Market(s)

Women 25-54 with children living at home, income over $150k/year

Industry/Entity Type

Clinic

Requirements
Must have
• Masthead incorporating the logo
Followed by the primary nav
Slider on the home page below that
Dual nav - 1 with the nav in the attached site map
2 secondary nav with areas of healthcare
There will three blocks under the nav
1. It's about time (with a small blurb less than 50 words.
2. It's about choices (with small blurb)
3. It's about you (with small blurb)
Three footer blocks
patient check in link on every page
"No appointment? No problem" icon on every page

```html
<!DOCTYPE html>
<html lang="en">
<head>
<meta charset="utf-8">
<title>Ashworth Medical</title>
<link href="https://fonts.googleapis.com/css2?family=Open+Sans:wght@400;600;700&family=Questrial&display=swap" rel="stylesheet">
<style>
:root{
  --blue:#175fa8;
  --green:#27b35c;
  --green-soft:#62c48c;
  --grey-box:#eeeeee;
  --grey-band:#f0f0f0;
  --text:#555;
  --dark:#333;
  --line:#dcdcdc;
}
*{margin:0;padding:0;box-sizing:border-box}
html,body{width:785px;height:1200px;overflow:hidden;background:#fff}
body{position:relative;font-family:"Open Sans",Arial,sans-serif;color:var(--text)}
.abs{position:absolute}
.masthead{left:0;top:0;width:785px;height:78px;background:linear-gradient(#f4f4f4,#fff)}
.brand{display:flex;align-items:center;gap:8px}
.brand-mark{width:40px;height:40px;border-radius:50%;background:var(--blue)}
.brand-name{font-family:"Open Sans",Arial,sans-serif;font-weight:700;color:var(--blue)}
.masthead .brand{left:94px;top:16px}
.masthead .brand-name{font-size:26px;letter-spacing:-.5px}
.tagline{left:146px;top:50px;font-size:8.5px;font-weight:700;color:#3a4a5a}
.account-links{left:565px;top:33px;display:flex;border:1px solid #d4d4d4;border-radius:10px;background:linear-gradient(#fff,#ececec);font-size:9px;color:var(--dark);height:18px;align-items:center}
.account-links span{padding:0 8px;border-right:1px solid #d4d4d4}
.account-links span:last-child{border:0}
.main-nav{left:92px;top:92px;display:flex;gap:24px;font-size:11.5px;color:var(--dark)}
.main-nav .current{color:var(--green)}
.nav-rule{left:92px;top:116px;width:601px;height:3px;background:var(--blue)}
.social-top{left:626px;top:91px;display:flex;gap:2px}
.social-top i{width:21px;height:21px;border-radius:50%;display:block}
.promo{top:125px;height:78px;background:var(--grey-box);padding:11px 11px 0}
.promo h2{font-family:"Questrial",sans-serif;font-weight:400;font-size:15px;color:var(--blue);margin-bottom:4px}
.promo h2 b{font-weight:700}
.promo p{font-size:8px;line-height:12px;color:#555}
.hero{left:0;top:211px;width:785px;height:337px;background:linear-gradient(100deg,#dfe7ee 0%,#c9a98a 35%,#e2c9a8 55%,#e8e4de 80%,#f0f2f3 100%)}
.caption{font-family:"Questrial",sans-serif;color:#fff;font-size:22px;height:30px;line-height:30px;padding:0 10px}
.caption.one{left:103px;top:404px;width:340px;background:var(--green);border-radius:8px 8px 0 0}
.caption.two{left:177px;top:433px;width:258px;background:var(--blue);border-radius:0 0 8px 8px}
.care-menu{left:92px;top:567px;width:142px;height:161px;border:1px solid #ddd;box-shadow:0 1px 4px rgba(0,0,0,.18);padding:4px 8px;list-style:none}
.care-menu li{font-size:9px;color:var(--dark);height:21.5px;line-height:21.5px;border-bottom:1px solid #e6e6e6;padding-left:14px;position:relative}
.care-menu li:last-child{border:0}
.care-menu li::before{content:"";position:absolute;left:4px;top:8px;border-left:4px solid var(--blue);border-top:3px solid transparent;border-bottom:3px solid transparent}
.welcome{left:247px;top:567px;width:243px;height:300px;background:var(--blue);border-radius:0 20px 0 20px;padding:9px 12px;color:#fff}
.welcome .small{font-family:"Questrial",sans-serif;font-size:13px}
.welcome h1{font-size:19px;font-weight:700;line-height:20px;margin-bottom:8px}
.welcome h1 span{color:var(--green)}
.welcome p{font-size:8.6px;line-height:14.1px}
.doctor-photo{left:503px;top:567px;width:69px;height:69px;background:linear-gradient(#e9eef2,#c9b7a4)}
.doctor-tag{left:572px;top:567px;width:73px;height:29px;background:var(--green);border-radius:0 14px 0 0;color:#fff;font-size:11px;line-height:12px;padding:3px 7px}
.doctor-role{left:581px;top:613px;font-family:"Questrial",sans-serif;color:var(--blue);font-size:10.5px;line-height:12px}
.doctor-bio{left:503px;top:643px;width:192px;font-size:8.6px;line-height:14.1px}
.care-band{left:0;top:875px;width:785px;height:118px;background:var(--grey-band)}
.care-badge{left:92px;top:892px;width:154px;height:76px;background:var(--green);border-radius:0 14px 0 0;color:#fff;font-size:15px;font-weight:700;line-height:19px;padding:10px 12px}
.care-copy{left:259px;top:889px;width:440px}
.care-copy h3{font-size:10.5px;font-weight:400;color:var(--dark);margin-bottom:6px}
.care-copy p{font-size:8.5px;line-height:14.1px}
.care-copy a{color:var(--blue);text-decoration:none}
.walkin-rule{left:92px;top:1027px;width:601px;height:1px;background:var(--line)}
.walkin{left:216px;top:1009px;width:344px;height:36px;border-radius:18px;background:var(--green-soft);color:#fff;font-family:"Questrial",sans-serif;font-size:21px;text-align:center;line-height:36px}
.connect{left:130px;top:1062px;width:88px;text-align:center;font-family:"Questrial",sans-serif;font-size:12px;letter-spacing:2.5px;line-height:13px;color:var(--dark)}
.social-foot{left:117px;top:1100px;display:flex;gap:14px}
.social-foot i{width:30px;height:30px;border-radius:4px;display:block}
.footer-brand{left:300px;top:1062px;width:185px;text-align:center}
.footer-brand .brand-mark{margin:0 auto 6px}
.footer-brand .brand-name{font-size:19px;letter-spacing:-.3px}
.footer-brand .tagline-foot{font-size:7px;font-weight:700;color:#3a4a5a}
.contact{left:525px;top:1064px;font-size:8.6px;line-height:14.2px;color:var(--dark)}
.contact .phone{font-family:"Questrial",sans-serif;font-size:18px;color:var(--green);line-height:22px;margin-bottom:6px}
.foot-rule{left:92px;top:1147px;width:601px;height:1px;background:var(--line)}
.foot-nav{left:227px;top:1158px;display:flex;gap:15px;font-size:9px;color:var(--dark)}
.copyright{left:0;top:1177px;width:785px;height:23px;background:#e3e3e3;font-size:8.5px;text-align:center;line-height:23px;color:var(--dark)}
</style>
</head>
<body>
<header class="abs masthead"></header>
<div class="abs brand"><span class="brand-mark"></span><span class="brand-name">Ashworth Medical</span></div>
<div class="abs tagline">Immediate Family and Personal Care</div>
<div class="abs account-links"><span>Register</span><span>Log In</span><span>Blog</span></div>

<nav class="abs main-nav">
  <span class="current">Home</span><span>About</span><span>Services</span><span>Staff</span><span>Insurance</span><span>Videos</span><span>Contact Us</span>
</nav>
<div class="abs social-top"><i style="background:#c9302c"></i><i style="background:#4fa9d8"></i><i style="background:#1b5aa6"></i></div>
<div class="abs nav-rule"></div>

<section class="abs promo" style="left:92px;width:196px"><h2>It's <b>About Time</b></h2><p>Lorem ipsum dolor sit amet, consectetur adipisicing elit, sed do eiusmod tempor incididunt ut labore.</p></section>
<section class="abs promo" style="left:295px;width:195px"><h2>It's <b>About Choices</b></h2><p>Lorem ipsum dolor sit amet, consectetur adipisicing elit, sed do eiusmod tempor incididunt.</p></section>
<section class="abs promo" style="left:497px;width:196px"><h2>It's <b>About You</b></h2><p>Lorem ipsum dolor sit amet, consectetur adipisicing elit, sed do eiusmod tempor incididunt ut labore et.</p></section>

<div class="abs hero" role="img" aria-label="Smiling family of four in front of a bright white house"></div>
<div class="abs caption one">Concierge-quality healthcare...</div>
<div class="abs caption two">...for your whole family</div>

<ul class="abs care-menu">
  <li>Immediate Care</li><li>Allergies</li><li>Primary Care</li><li>Women's Health</li><li>Medical Spa Treatments</li><li>Men's Health</li><li>Weight Loss</li>
</ul>

<section class="abs welcome">
  <div class="small">Welcome to</div>
  <h1>Ashworth<span>Medical</span></h1>
  <p>Sed ut perspiciatis unde omnis iste natus error sit voluptatem accusantium doloremque laudantium, totam rem aperiam, eaque ipsa quae ab illo inventore veritatis et quasi architecto beatae vitae dicta sunt explicabo. Nemo enim ipsam voluptatem quia voluptas sit aspernatur aut odit aut fugit, sed quia consequuntur magni dolores eos qui ratione voluptatem sequi nesciunt. Neque porro quisquam est, qui dolorem ipsum quia dolor sit amet, consectetur, adipisci velit, sed quia non numquam eius modi tempora incidunt ut labore et dolore magnam aliquam quaerat voluptatem. Ut enim ad minima veniam, quis nostrum exercitationem ullam corporis suscipit laboriosam, nisi ut aliquid ex ea commodi consequatur? Quis autem vel eum iure reprehenderit qui in ea voluptate velit esse quam nihil molestiae consequatur.</p>
</section>

<div class="abs doctor-photo" role="img" aria-label="Portrait of the family physician in a white coat"></div>
<div class="abs doctor-tag">Elliot R.<br>Vance, MD</div>
<div class="abs doctor-role">Your new<br>family physician</div>
<p class="abs doctor-bio">Lorem ipsum dolor sit amet, consectetur adipisicing elit, sed do eiusmod tempor incididunt ut labore et dolore magna aliqua. Ut enim ad minim veniam, quis nostrud exercitation ullamco laboris nisi ut aliquip ex ea commodo consequat. Duis aute irure dolor in reprehenderit in voluptate velit esse cillum dolore eu fugiat nulla pariatur. Excepteur sint occaecat cupidatat non proident, sunt in culpa qui officia deserunt mollit anim id est laborum.</p>

<div class="abs care-band"></div>
<div class="abs care-badge">Convenient<br>Comprehensive<br>Care</div>
<div class="abs care-copy">
  <h3>Long waits. Short office hours. What happened to the "care" in healthcare?</h3>
  <p>Your health is important to you. It's important to us, too. You're the reason we're here with comprehensive compassionate healthcare services for you and your entire family. We believe to make healthcare really work. It has to start with a relationship based on trust, respect, and understanding. That means we do everything in our power, including extending our hours, to make the time you spend at Ashworth Medical positive and productive. <a href="#">Read more...</a></p>
</div>

<div class="abs walkin-rule"></div>
<div class="abs walkin">No appointment? No problem</div>

<div class="abs connect">CONNECT<br>WITH US</div>
<div class="abs social-foot"><i style="background:#3b5a9a"></i><i style="background:#5aaedc"></i><i style="background:#1c79b5"></i></div>

<div class="abs footer-brand">
  <span class="brand-mark" style="display:block"></span>
  <div class="brand-name">Ashworth Medical</div>
  <div class="tagline-foot">Immediate Family and Personal Care</div>
</div>

<address class="abs contact" style="font-style:normal">
  <div class="phone">(555) 014 2270</div>
  AshworthFamilyMedical.example<br>
  4120 Linden Ave (at Oak Pkwy) Ste 180,<br>
  Dallas, TX 75001
</address>

<div class="abs foot-rule"></div>
<nav class="abs foot-nav"><span>Home</span><span>About</span><span>Services</span><span>Staff</span><span>Insurance</span><span>Videos</span><span>Contact Us</span></nav>
<footer class="abs copyright">© 2012 AshworthMedical. All Rights Reserved</footer>
</body>
</html>
```